Page Layouts for Australian Political Party

The Forward Signal Party of Australia has a design for its logo and now is looking for a website proposal. The initial website is being powered by blogger with plans to move to an ExpressionEngine based site. The current website is at www.fspartyhub.org

Its likely if we see a design within the next 2 days we like it will be selected before the 5 days has expired.

Target Market(s)

Looking for a design that will appeal to both the "online" generation as well as more casual internet users. These users might be comfortable with online banking and perhaps mailnest/talkloop but not much more.

I personally like the "feel" of vimrol.com and plumtreelabs.com. You might like to look at the other major political parties in Australia to see what probably quite a lot of "market testing" and money is acceptable to the Australian population. We are aiming for Generation X and younger and well as the baby boomers who get the 2.0 internet.

Industry/Entity Type

Political

Requirements
Must have
• The ability to scale elegantly across a full ExpressionEngine implementation, forums, blogs, homepage etc.
• Also look elegant on the initial blogger driven page.
• Navigation that could contain all the items on the www.unityfront.org.au site, you can use these as the place holder names for the navigation design. The short name for the party is FSP. The
Nice to have
• feel distinct from the other major parties websites. we do have views more in line with the orchardists/reformists in this country.
Should not have
• basic stuff, not look like a pagenook page ;) imagery too similar from any of the other parties...

```html
<!DOCTYPE html>
<html lang="en">
<head>
<meta charset="utf-8">
<title>Forward Signal Party of Australia</title>
<link rel="stylesheet" href="https://fonts.googleapis.com/css2?family=Arimo:ital,wght@0,400;0,700;1,400&display=swap">
<style>
  :root {
    --header-top: #f4f2ed;
    --header-mid: #ece9e2;
    --header-bottom: #dcd9cf;
    --tab-top: #ffffff;
    --tab-bottom: #dde8f4;
    --tab-border: #b9c3cf;
    --tab-text: #333333;
    --sky-band: #88d5f3;
    --sky-band-deep: #77cbee;
    --cream: #fbf8f1;
    --cream-warm: #f6e4bf;
    --ink: #1d1d1d;
    --lead-red: #6d0f12;
    --link-red: #7a0d0d;
    --navy: #121d63;
    --white: #ffffff;
    --gold-top: #ffe27a;
    --gold-bottom: #efb429;
    --brand-blue: #1f3f94;
    --social-top: #f7f9fc;
    --social-bottom: #cfdbe8;
    --social-edge: #a9b8ca;
  }
  * { margin: 0; padding: 0; box-sizing: border-box; }
  html, body { width: 1200px; height: 937px; overflow: hidden; }
  body {
    position: relative;
    font-family: "Arimo", Arial, sans-serif;
    color: var(--ink);
    background: var(--white);
  }

  .site-header {
    position: absolute; left: 0; top: 0; width: 1200px; height: 192px;
    background: linear-gradient(to bottom, var(--header-top), var(--header-mid) 60%, var(--header-bottom));
  }
  .brand {
    position: absolute; left: 129px; top: 104px;
    display: flex; align-items: center; gap: 12px;
  }
  .brand-mark {
    width: 22px; height: 22px; border-radius: 4px;
    background: var(--brand-blue);
  }
  .brand-name {
    font-size: 30px; font-weight: 400; letter-spacing: -0.6px;
    color: #2b2b2b; white-space: nowrap; line-height: 34px;
  }
  .brand-tagline {
    position: absolute; left: 163px; top: 84px;
    font-size: 11px; letter-spacing: 1.6px; color: #6a6a6a;
    text-transform: uppercase;
  }

  .search {
    position: absolute; left: 678px; top: 63px;
    display: flex; align-items: center; gap: 11px;
  }
  .search-field {
    width: 261px; height: 25px; background: var(--white);
    border: 1px solid #8c8a6a; border-right-color: #ddd; border-bottom-color: #ddd;
  }
  .search-button {
    width: 94px; height: 24px; border-radius: 12px;
    background: linear-gradient(to bottom, var(--gold-top), var(--gold-bottom));
    box-shadow: inset 0 -1px 0 rgba(160,110,0,0.35);
    font-size: 11.5px; color: #3a2a00; text-align: center; line-height: 24px;
    letter-spacing: 0.4px;
  }
  .social {
    position: absolute; left: 895px; top: 104px;
    display: flex; gap: 7px;
  }
  .social a {
    width: 25px; height: 25px; border-radius: 5px;
    background: linear-gradient(to bottom, var(--social-top), var(--social-bottom));
    border: 1px solid var(--social-edge);
    display: flex; align-items: center; justify-content: center;
  }
  .social a span {
    width: 9px; height: 9px; border-radius: 50%;
    background: #7d93ad;
  }

  .main-nav {
    position: absolute; left: 125px; top: 147px; width: 953px; height: 45px;
    display: flex;
  }
  .main-nav a {
    flex: 1; height: 45px;
    background: linear-gradient(to bottom, var(--tab-top), var(--tab-bottom));
    border: 1px solid var(--tab-border); border-bottom: none;
    border-radius: 8px 8px 0 0;
    font-size: 13px; font-weight: 700; color: var(--tab-text);
    text-decoration: none; text-align: center; line-height: 44px;
  }

  .hero-backdrop {
    position: absolute; left: 0; top: 192px; width: 1200px; height: 367px;
    background: linear-gradient(to right, #ffffff 0%, #eaf3fa 10%, #f5f9fc 50%, #e4eff8 90%, #ffffff 100%);
  }
  .hero-photo {
    position: absolute; left: 123px; top: 192px; width: 954px; height: 367px;
    background:
      linear-gradient(to right, rgba(70,90,130,0.55) 0%, rgba(70,90,130,0.15) 30%, rgba(0,0,0,0) 45%),
      linear-gradient(to bottom,
        #9fc0e4 0%, #c4d8ec 30%, #e3ecf4 48%,
        #a7b98a 56%, #7f9468 60%,
        #b9a9a2 64%, #8f9fbd 76%, #4e628c 90%, #34456e 100%);
  }

  .feature-band {
    position: absolute; left: 0; top: 559px; width: 1200px; height: 272px;
    background: linear-gradient(to bottom, var(--sky-band), var(--sky-band-deep));
  }
  .about-panel {
    position: absolute; left: 124px; top: 578px; width: 465px; height: 233px;
    background: radial-gradient(ellipse at 85% 0%, var(--cream-warm) 0%, var(--cream) 55%);
  }
  .section-title {
    font-size: 29px; font-weight: 400; letter-spacing: -0.8px; color: #1a1a1a;
  }
  .about-panel .section-title { position: absolute; left: 67px; top: 24px; }
  .about-lead {
    position: absolute; left: 74px; top: 72px; width: 360px;
    font-size: 14px; font-style: italic; line-height: 18px; color: var(--lead-red);
  }
  .about-body {
    position: absolute; left: 74px; top: 112px; width: 360px;
    font-size: 13px; line-height: 18.6px; color: #222;
  }
  .read-more {
    position: absolute; left: 74px; top: 184px;
    font-size: 14px; font-weight: 700; color: var(--link-red);
    text-decoration: underline; display: flex; align-items: center; gap: 9px;
  }

  .services .section-title { position: absolute; left: 638px; top: 602px; }
  .service {
    position: absolute; display: flex; gap: 22px; width: 400px;
    font-size: 13px; line-height: 18.6px; color: #1f2a33;
  }
  .service strong { color: #1a1a1a; }
  .service-icon { flex: none; width: 56px; height: 52px; }
  .service-one { left: 640px; top: 656px; }
  .service-one .service-icon { border-radius: 50%; background: radial-gradient(circle at 40% 40%, #f07a5a, #c3281d); }
  .service-one p { width: 280px; padding-top: 3px; }
  .service-two { left: 640px; top: 723px; }
  .service-two .service-icon { border-radius: 10px; background: linear-gradient(135deg, #3aa7e0, #f0a23a); }
  .service-two p { width: 310px; padding-left: 6px; }

  .site-footer {
    position: absolute; left: 0; top: 831px; width: 1200px; height: 106px;
    background: var(--navy);
  }
  .footer-nav {
    position: absolute; left: 175px; top: 31px;
    display: flex; font-size: 13.5px; color: var(--white);
  }
  .footer-nav a { color: var(--white); text-decoration: none; }
  .footer-nav .sep { margin: 0 21px; }
</style>
</head>
<body>
  <header class="site-header">
    <a class="brand" href="#">
      <span class="brand-mark"></span>
      <span class="brand-name">Forward Signal</span>
    </a>
    <div class="search">
      <span class="search-field"></span>
      <span class="search-button">SEARCH</span>
    </div>
    <div class="social" aria-label="Social links">
      <a href="#" aria-label="Social link"><span></span></a>
      <a href="#" aria-label="Social link"><span></span></a>
      <a href="#" aria-label="Social link"><span></span></a>
      <a href="#" aria-label="Social link"><span></span></a>
      <a href="#" aria-label="News feed"><span></span></a>
    </div>
    <nav class="main-nav">
      <a href="#">THE PARTY</a>
      <a href="#">LATEST NEWS</a>
      <a href="#">ECONOMY</a>
      <a href="#">COMMUNITY</a>
      <a href="#">SENIORS</a>
      <a href="#">HEALTH</a>
      <a href="#">CONTACT US</a>
    </nav>
  </header>

  <div class="hero-backdrop"></div>
  <div class="hero-photo" role="img" aria-label="Photo of a group of young friends sitting together on grass under a bright sky"></div>

  <section class="feature-band"></section>

  <section class="about-panel">
    <h2 class="section-title">What We Do...</h2>
    <p class="about-lead">Vestibulum iaculis lacinia est. Proin dictum elementum velit. Fusce euismod consequat ante.</p>
    <p class="about-body">Maecenas tristique orci ac sem. Duis ultricies pharetra magna. Donec accumsan malesuada orci. Donec sit amet eros. Lorem ipsum dolor sit amet, consectetuer adipiscing</p>
    <a class="read-more" href="#">
      <svg width="5" height="8" viewBox="0 0 5 8"><path d="M0 0 L5 4 L0 8 Z" fill="#7a0d0d"/></svg>
      Click here to read more
    </a>
  </section>

  <section class="services">
    <h2 class="section-title">Our Services</h2>
    <div class="service service-one">
      <span class="service-icon" role="img" aria-label="Red chart illustration"></span>
      <p><strong>Donec sit amet eros.</strong> Lorem ipsum dolor sit amet, consectetuer adipiscing elit.</p>
    </div>
    <div class="service service-two">
      <span class="service-icon" role="img" aria-label="Building blocks illustration"></span>
      <p><strong>Sed laoreet aliquam leo.</strong> Ut tellus dolor, dapibus eget, elementum vel, cursus eleifend elit. Aenean auctor wisi et urna.</p>
    </div>
  </section>

  <footer class="site-footer">
    <nav class="footer-nav">
      <a href="#">Main page</a><span class="sep">|</span>
      <a href="#">About us</a><span class="sep">|</span>
      <a href="#">Services</a><span class="sep">|</span>
      <a href="#">Solutions</a><span class="sep">|</span>
      <a href="#">Contact us</a><span class="sep">|</span>
      <a href="#">Privacy policy</a>
    </nav>
  </footer>
</body>
</html>
```